Brindlewave Consulting Limited needs a Brochure/ Company Profile

We need a Company profile for our IT consulting company. We need to layout the brochure in a very unique and creative way that is captivating to any audience and fun to read. Our website gives a description of what we offer. www.brindlewaveconsults.example. The site also shows our color scheme. The Brochure will have the following main headings. (Please review the attachment for most of th content). Please note that these are the headings expected to be in each major section of the brochure so should form a table of content
1. Executive Summary
2. Philosophy
3. BCL Corporate Structure
4. BCL Capabilities
5. BCL Offerings
6. Industry Milestones
7. Management Team
8. Partners and Tools
This list is not exhaustive but should give a general idea of the direction.
Updates
Target Market(s)
Banking, Manufacturing, Small Businesses, Government
Industry/Entity Type
It Company
Requirements
Must have
- Size should be slightly smaller than A3 folded in halve. There should be a catchy professional looking frontpage and a simple backpage
Nice to have
- Networking Images, drawings, vector images /pictures that represent Information Technology, Networking, Computing, Unified Communications
Should not have
- The brochure must not contain any images from the website expect the company logo and must not have any pictures of individuals.
- There should not be any pictures copied from the website. Only images /picture that represent Information Technology, Networking, Computing, Unified Communications e.t.c should be in the brochure.

```html
<!DOCTYPE html>
<html lang="en">
<head>
<meta charset="utf-8">
<title>Brindlewave Consulting Limited – Company Profile Spread</title>
<link rel="stylesheet" href="https://fonts.googleapis.com/css2?family=Montserrat:wght@700;800&family=Open+Sans:wght@400;600&display=swap">
<style>
  :root{
    --backdrop:#e4e4e2;
    --paper:#ffffff;
    --ink:#4a4f55;
    --ink-soft:#7b8087;
    --teal:#2f4f5e;
    --orange:#e0692b;
    --rule:#c9ccd0;
    --tone-blue:#4a74a8;
    --tone-red:#b23a31;
    --tone-gold:#e3a532;
    --tone-green:#4e9b7c;
  }
  *{box-sizing:border-box;margin:0;padding:0}
  html,body{width:1200px;height:804px;overflow:hidden;background:var(--backdrop)}
  body{font-family:"Open Sans",Arial,sans-serif;color:var(--ink)}
  .spread{position:absolute;left:60px;top:20px;width:1080px;height:764px;display:flex;box-shadow:0 6px 24px rgba(0,0,0,.18)}
  .page{position:relative;width:540px;height:764px;background:var(--paper);overflow:hidden}
  .page--left{background:linear-gradient(to right,#fff 92%,#eceded)}
  .page--right{background:linear-gradient(to left,#fff 92%,#eceded)}

  .masthead{position:absolute;top:22px;left:0;width:540px;height:26px}
  .masthead__band{position:absolute;left:0;top:0}
  .masthead__tagline{position:absolute;left:22px;top:7px;font-size:8.5px;color:#fff;font-weight:600;letter-spacing:.1px}
  .brand{position:absolute;right:22px;top:6px;display:flex;align-items:center;gap:4px;font-family:"Montserrat",sans-serif;font-weight:700;font-size:9.5px;color:var(--teal);letter-spacing:.6px}
  .brand__dot{width:10px;height:10px;border-radius:50%;background:var(--teal)}

  .heading{position:absolute;left:40px;font-family:"Montserrat",sans-serif;font-weight:800;font-size:19px;color:var(--teal);letter-spacing:-.2px;text-transform:uppercase}
  .heading__accent{color:var(--orange)}

  .copy{position:absolute;left:40px;width:462px;font-size:8.6px;line-height:1.5}
  .copy p{margin-bottom:8px}

  .steps{list-style:none;margin-top:2px}
  .steps li{display:flex;align-items:center;gap:7px;margin-bottom:3px}
  .steps svg{flex:none}

  .photo{position:absolute;left:0;top:318px;width:540px;height:200px;background:linear-gradient(100deg,#3a3f4a 0%,#8a8f99 35%,#d8d8d6 55%,#6b7482 80%,#c4cbd6 100%)}
  .photo__corner{position:absolute;left:0;top:486px}

  .structure-art{position:absolute;left:40px;top:390px;width:462px;height:290px;
    background:linear-gradient(110deg,
      rgba(74,116,168,.55) 0%,
      rgba(178,58,49,.5) 30%,
      rgba(227,165,50,.55) 55%,
      rgba(78,155,124,.55) 80%,
      rgba(255,255,255,.6) 100%);}

  .footer{position:absolute;left:30px;right:30px;bottom:26px;border-top:1px solid var(--rule);padding-top:6px;font-size:5.6px;color:var(--ink-soft);letter-spacing:0;white-space:nowrap}
  .footer__num{position:absolute;right:6px;top:-16px;font-size:9px;color:var(--ink)}
</style>
</head>
<body>
<main class="spread">

  <section class="page page--left">
    <header class="masthead">
      <svg class="masthead__band" width="420" height="26" viewBox="0 0 420 26"><polygon points="0,0 405,0 420,26 0,26" fill="var(--teal)"/></svg>
      <span class="masthead__tagline">Innovative information technology and project management solutions</span>
      <div class="brand"><span class="brand__dot"></span>BRINDLEWAVE</div>
    </header>

    <h2 class="heading" style="top:68px">Executive <span class="heading__accent">Summary</span></h2>

    <div class="copy" style="top:108px">
      <p>Brindlewave Consulting Limited offers innovative information technology and project management solutions locally in Nigeria and internationally across Africa, Middle East and Asia. Our portfolio covers a wide range of markets from small to large scale businesses, the financial sector, telecommunications industry, engineering and government.</p>
      <p>Our core strength is the provision of converged and resilient IT solutions using the available resources best suited for your needs<br>We possess among the finest set of skills in the industry for IT Advisory, Project rollout, infrastructure support and training.</p>
      <p>We follow 3 basic steps to solution delivery</p>
      <ul class="steps">
        <li><svg width="10" height="10" viewBox="0 0 10 10"><rect x=".5" y=".5" width="9" height="9" fill="none" stroke="var(--orange)"/><path d="M2 5l2 2 4-5" fill="none" stroke="var(--orange)" stroke-width="1.6"/></svg>We take your requirements,</li>
        <li><svg width="10" height="10" viewBox="0 0 10 10"><rect x=".5" y=".5" width="9" height="9" fill="none" stroke="var(--orange)"/><path d="M2 5l2 2 4-5" fill="none" stroke="var(--orange)" stroke-width="1.6"/></svg>We convert your requirements into solutions.</li>
        <li><svg width="10" height="10" viewBox="0 0 10 10"><rect x=".5" y=".5" width="9" height="9" fill="none" stroke="var(--orange)"/><path d="M2 5l2 2 4-5" fill="none" stroke="var(--orange)" stroke-width="1.6"/></svg>We bring those solutions to life.</li>
      </ul>
    </div>

    <div class="photo" role="img" aria-label="Photograph of a business team meeting around a laptop in an office"></div>
    <svg class="photo__corner" width="540" height="34" viewBox="0 0 540 34">
      <polygon points="0,32 540,0 540,34 0,34" fill="var(--paper)"/>
      <polygon points="438,26 468,0 506,14" fill="var(--orange)"/>
    </svg>

    <h2 class="heading" style="top:545px">Philosophy</h2>
    <div class="copy" style="top:580px">
      <p>We believe technology should serve people and processes, not the other way round. Every engagement starts with listening, continues with careful design and ends with systems our clients can run with confidence.</p>
      <p>Our teams combine deep local knowledge with international standards of delivery. We plan projects in clear stages, share progress openly and measure success by the value our clients see in their daily operations. We invest in training, keep our methods simple and stay with our clients long after go-live, supporting upgrades, audits and the steady growth of their infrastructure across banking, manufacturing and government.</p>
    </div>

    <footer class="footer"><span class="footer__num">4</span>BRINDLEWAVE CONSULTING LIMITED, Plot 7 Block 3 Harbour View Road, Marina District, Lagos. Telephone : +234 800 555 0192, E-mail : info@brindlewaveconsults.example</footer>
  </section>

  <section class="page page--right">
    <header class="masthead">
      <svg class="masthead__band" width="420" height="26" viewBox="0 0 420 26"><polygon points="0,0 405,0 420,26 0,26" fill="var(--teal)"/></svg>
      <span class="masthead__tagline">Innovative information technology and project management solutions</span>
      <div class="brand"><span class="brand__dot"></span>BRINDLEWAVE</div>
    </header>

    <h2 class="heading" style="top:68px">BCL Corporate <span class="heading__accent">Structure</span></h2>

    <div class="copy" style="top:104px">
      <p>Brindlewave is organised around clear lines of responsibility, so every client knows who owns each part of their project and who to call when a decision is needed.</p>
      <p>The board sets direction and reviews performance each quarter. Below it, the managing director leads four units: advisory, project delivery, infrastructure support and training. Each unit head reports progress weekly and shares resources across teams when client demand rises.</p>
      <p>Advisory consultants assess needs and shape solutions with the client. Project managers turn those plans into schedules, budgets and milestones. Engineers in the infrastructure unit build, test and maintain networks, servers and communication systems, while the training unit prepares client staff to use and manage every new system. Shared services in finance, procurement and quality assurance support all four units, keeping delivery consistent and costs under control throughout each engagement.</p>
    </div>

    <div class="structure-art" role="img" aria-label="Illustration of four numbered coloured blocks representing the corporate structure units, with short callout labels"></div>

    <footer class="footer"><span class="footer__num">5</span>BRINDLEWAVE CONSULTING LIMITED, Plot 7 Block 3 Harbour View Road, Marina District, Lagos. Telephone : +234 800 555 0192, E-mail : info@brindlewaveconsults.example</footer>
  </section>

</main>
</body>
</html>
```